Australian Natural Therpaist needs a light, fun, inviting wordpress website!

I need a wordpress website for my natural therapies business. I have already purchased the "vesk" theme from quillframestudio.com and so ideally this is what I would like to use.

The website will have the following pages:
1) Home
2) About Me
3) How I can help you
4) Contact Me
5) FAQ
6) Client Stories
7) Blog

I have attached a Balsamiq XML mockup and PDF of the homepage

I want the website to be very friendly and to de-mystify natural therapies/energy healing etc. I would like to keep the hand drawn/cartoon concept as it keeps everything light. My blog posts will consist of hand drawings and cartoons along with the blog text and so this would tie in with the look and feel of the website.

The homepage should have a slider at the top so that I can promote different concepts. The mockup shows an example of one of the advertising concepts I would use.

The website should make you feel light, it should be fun. No unicorns or rainbows. Here is a great example of what I DO NOT WANT http://www.copperwillowarts.com/

```html
<!DOCTYPE html>
<html lang="en">
<head>
<meta charset="utf-8">
<title>Marcus Fielding – Natural Therapies</title>
<link rel="stylesheet" href="https://fonts.googleapis.com/css2?family=Raleway:wght@300;400;500&display=swap">
<style>
:root{
  --accent:#3d8bb5;
  --icon:#8fb9d2;
  --ink:#333;
  --muted:#888;
  --card:#e6e6e6;
  --footer:#c0c0c0;
  --white:#fff;
  --band:rgba(0,0,0,.72);
}
*{margin:0;padding:0;box-sizing:border-box}
html,body{width:980px;height:1200px;overflow:hidden;background:var(--white);font-family:'Raleway',sans-serif;color:var(--ink)}
.site{position:relative;width:980px;height:1200px}
.site-header{height:86px;position:relative}
.brand{position:absolute;left:56px;top:20px}
.brand-name{font-size:27px;font-weight:400;color:var(--accent);letter-spacing:.2px}
.brand-name .surname{color:var(--muted);font-weight:300}
.brand-tagline{font-size:11px;color:var(--muted);margin-top:2px;margin-left:1px}
.main-nav{position:absolute;right:56px;top:37px;display:flex;gap:21px;font-size:12.5px}
.main-nav a{color:var(--ink);text-decoration:none}
.main-nav a.current{color:var(--accent)}
.hero{position:relative;height:534px;overflow:hidden}
.hero-art{position:absolute;inset:0;background:
  radial-gradient(ellipse 260px 200px at 40% 55%,rgba(170,215,255,.9),rgba(40,110,220,.6) 45%,transparent 75%),
  radial-gradient(ellipse 380px 180px at 65% 82%,rgba(230,170,110,.85),transparent 70%),
  linear-gradient(180deg,#020818 0%,#0a2a6a 45%,#1a4fa8 70%,#0a1a40 100%)}
.hero-caption{position:absolute;left:0;right:0;bottom:0;height:97px;background:var(--band);color:var(--white)}
.hero-title{position:absolute;left:77px;top:18px;font-size:25px;font-weight:400;letter-spacing:.3px}
.hero-text{position:absolute;left:77px;top:56px;width:700px;font-size:12px;line-height:17px;font-weight:300;color:#ddd}
.slider-controls{position:absolute;right:56px;top:25px;display:flex;gap:7px}
.slider-btn{width:41px;height:47px;background:#000;display:flex;align-items:center;justify-content:center}
.features{position:absolute;left:56px;top:661px;width:868px;display:grid;grid-template-columns:repeat(3,276px);column-gap:20px;row-gap:25px}
.feature{position:relative;height:182px;background:var(--card)}
.feature-title{position:absolute;left:13px;top:20px;font-size:23px;font-weight:400;color:#222}
.feature-icon{position:absolute;left:11px;top:58px;width:86px;height:86px}
.feature-text{position:absolute;left:108px;top:60px;width:162px;font-size:16.5px;line-height:26px;font-weight:300;color:#777}
.feature-more{position:absolute;right:17px;bottom:17px;width:21px;height:21px}
.site-footer{position:absolute;left:0;right:0;top:1083px;bottom:0;background:var(--footer)}
.social{position:absolute;left:58px;top:41px;display:flex;gap:5px}
.social-dot{width:36px;height:36px;border-radius:50%;background:#9a9a9a;border:2px solid #b8b8b8}
.footer-nav{position:absolute;right:103px;top:51px;font-size:13px;color:#555}
.footer-nav a{color:#555;text-decoration:none}
.footer-nav .sep{margin:0 6px}
</style>
</head>
<body>
<div class="site">
  <header class="site-header">
    <div class="brand">
      <div class="brand-name">Marcus <span class="surname">Fielding</span></div>
      <div class="brand-tagline">Healer - Helper- Mentro - &nbsp;Freind</div>
    </div>
    <nav class="main-nav">
      <a class="current" href="#">Home</a>
      <a href="#">About Me</a>
      <a href="#">How I can help you</a>
      <a href="#">Contact Me</a>
      <a href="#">FAQ</a>
      <a href="#">Client Stories</a>
      <a href="#">Blog</a>
    </nav>
  </header>

  <section class="hero">
    <div class="hero-art" role="img" aria-label="Open hand reaching up into a deep blue night glow with bright sparkling stars"></div>
    <div class="hero-caption">
      <h1 class="hero-title">LOREM IPSUM DOLOR SIT AMET</h1>
      <p class="hero-text">Consectetur adipisicing elit, sed do eiusmod tempor incididunt ut labore et dolore magna aliqua. Ut enim ad minim veniam, quis nostrud exercitation ullamco laboris nisi ut aliquip e</p>
      <div class="slider-controls">
        <div class="slider-btn"><svg width="14" height="28" viewBox="0 0 14 28"><path d="M12 1 L3 14 L12 27" fill="none" stroke="#fff" stroke-width="1.5"/></svg></div>
        <div class="slider-btn"><svg width="14" height="28" viewBox="0 0 14 28"><path d="M2 1 L11 14 L2 27" fill="none" stroke="#fff" stroke-width="1.5"/></svg></div>
      </div>
    </div>
  </section>

  <main class="features">
    <article class="feature">
      <h2 class="feature-title">About Me</h2>
      <svg class="feature-icon" viewBox="0 0 86 86"><g fill="none" stroke="var(--icon)" stroke-width="2"><ellipse cx="44" cy="26" rx="17" ry="21"/><path d="M2 84 C4 64 18 58 32 54 L34 46 M54 46 L56 54 C70 58 84 64 86 84 Z"/></g></svg>
      <p class="feature-text">Who is this Marcus Fielding? Whats his story</p>
      <svg class="feature-more" viewBox="0 0 22 22"><circle cx="11" cy="11" r="10" fill="none" stroke="var(--accent)" stroke-width="1.3"/><path d="M11 6v10M6 11h10" stroke="var(--accent)" stroke-width="1.4"/></svg>
    </article>
    <article class="feature">
      <h2 class="feature-title">How I can help you</h2>
      <svg class="feature-icon" viewBox="0 0 86 86"><g fill="var(--icon)"><path d="M38 4c14 0 22 7 22 17 0 9-6 12-11 15-3 2-3 4-3 7h-10c0-6 1-9 6-12 4-3 7-4 7-9 0-4-3-7-10-7-6 0-9 3-10 8l-10-2C21 10 28 4 38 4z"/><rect x="35" y="47" width="11" height="9"/><path d="M10 86c0-18 12-26 31-26s31 8 31 26z"/></g><path d="M41 62l-4 6 4 14 4-14z" fill="#fff"/></svg>
      <p class="feature-text">Who is this Marcus Fielding? Whats his story</p>
      <svg class="feature-more" viewBox="0 0 22 22"><circle cx="11" cy="11" r="10" fill="none" stroke="var(--accent)" stroke-width="1.3"/><path d="M11 6v10M6 11h10" stroke="var(--accent)" stroke-width="1.4"/></svg>
    </article>
    <article class="feature">
      <h2 class="feature-title">I have questions</h2>
      <svg class="feature-icon" viewBox="0 0 86 86"><circle cx="43" cy="43" r="34" fill="none" stroke="var(--icon)" stroke-width="3"/><text x="43" y="60" text-anchor="middle" font-family="Raleway,sans-serif" font-size="48" font-weight="500" fill="var(--icon)">?</text></svg>
      <p class="feature-text">Who is this Marcus Fielding? Whats his story</p>
      <svg class="feature-more" viewBox="0 0 22 22"><circle cx="11" cy="11" r="10" fill="none" stroke="var(--accent)" stroke-width="1.3"/><path d="M11 6v10M6 11h10" stroke="var(--accent)" stroke-width="1.4"/></svg>
    </article>
    <article class="feature">
      <h2 class="feature-title">Client Stories</h2>
      <svg class="feature-icon" viewBox="0 0 86 86"><g fill="var(--card)" stroke="var(--icon)" stroke-width="2.2"><path d="M52 34c14 0 30 6 30 16 0 5-3 8-6 10l3 9-10-6c-5 2-11 2-17 1-10-2-18-7-18-14 0-10 10-16 18-16z"/><path d="M34 8c17 0 32 8 32 19s-15 19-32 19c-4 0-8 0-11-1L10 52l4-10C8 38 3 33 3 27 3 16 17 8 34 8z"/></g></svg>
      <p class="feature-text">Who is this Marcus Fielding? Whats his story</p>
      <svg class="feature-more" viewBox="0 0 22 22"><circle cx="11" cy="11" r="10" fill="none" stroke="var(--accent)" stroke-width="1.3"/><path d="M11 6v10M6 11h10" stroke="var(--accent)" stroke-width="1.4"/></svg>
    </article>
    <article class="feature">
      <h2 class="feature-title">Blog</h2>
      <svg class="feature-icon" viewBox="0 0 86 86"><g fill="none" stroke="var(--icon)" stroke-width="5" stroke-linejoin="round"><path d="M10 8h42l16 16v56H10z"/><path d="M52 8v16h16"/><path d="M22 40h34M22 52h34M22 64h22"/></g></svg>
      <p class="feature-text">Who is this Marcus Fielding? Whats his story</p>
      <svg class="feature-more" viewBox="0 0 22 22"><circle cx="11" cy="11" r="10" fill="none" stroke="var(--accent)" stroke-width="1.3"/><path d="M11 6v10M6 11h10" stroke="var(--accent)" stroke-width="1.4"/></svg>
    </article>
    <article class="feature">
      <h2 class="feature-title">Contact Me</h2>
      <svg class="feature-icon" viewBox="0 0 86 86"><circle cx="43" cy="43" r="38" fill="none" stroke="var(--icon)" stroke-width="4"/><path d="M30 20l8-2 5 13-6 4c2 7 7 14 13 18l5-5 12 7-2 8c-3 3-8 4-13 1-12-7-21-19-25-31-2-6 0-11 3-13z" fill="none" stroke="var(--icon)" stroke-width="3.5" stroke-linejoin="round"/></svg>
      <p class="feature-text">Who is this Marcus Fielding? Whats his story</p>
      <svg class="feature-more" viewBox="0 0 22 22"><circle cx="11" cy="11" r="10" fill="none" stroke="var(--accent)" stroke-width="1.3"/><path d="M11 6v10M6 11h10" stroke="var(--accent)" stroke-width="1.4"/></svg>
    </article>
  </main>

  <footer class="site-footer">
    <div class="social">
      <span class="social-dot"></span>
      <span class="social-dot"></span>
      <span class="social-dot"></span>
      <span class="social-dot"></span>
    </div>
    <nav class="footer-nav">
      <a href="#">Home</a><span class="sep">|</span><a href="#">About</a><span class="sep">|</span><a href="#">Sitemap</a>
    </nav>
  </footer>
</div>
</body>
</html>
```